Quillby Systems Business Card

Create an appealing and elegant Business card for quillby systems. Include logo and use related colors from website, be creative. Include Business name, my name, tile, address, contacts, address, and social media contacts if possible. Logo PSD file is attached.

Bleed Area: 3.46" x 2.32"
Trim: 3.3" x 2.16"
Safe Area: 3.14" x 2.02"

Save files as vector-based PDF with outlined text and PNG.
No crop marks
CMYK color setting

Business Card Info:

Quillby Systems

Dorian Vellacott
Owner

418 Bramlow Rd Unit C
Fernmoor, QS 02771
t. 1.888.562.3907
e. dorian.v@quillbysys.example
w. www.quillbysys.example

facebook. www.facebook.com/QuillbySys
twitter. twitter.com/quillbysys
pinterest. www.pinterest.com/quillbysys/

Target Market(s)

Business Owners and Partners

Industry/Entity Type

Business

Requirements
Must have
• Logo and related colors from website

```html
<!DOCTYPE html>
<html lang="en">
<head>
<meta charset="utf-8">
<title>Quillby Systems Business Card</title>
<link href="https://fonts.googleapis.com/css2?family=Open+Sans:wght@400;600;700&display=swap" rel="stylesheet">
<style>
  :root {
    --backdrop: #2a2a2d;
    --paper: #ffffff;
    --paper-soft: #f2f2f2;
    --ink: #1d1d1f;
    --ink-soft: #3a3a3c;
    --brand-blue: #4a70a6;
    --brand-blue-deep: #3d5f8f;
    --charcoal: #2e2e31;
    --band: #1b1b1d;
  }
  * { box-sizing: border-box; margin: 0; padding: 0; }
  html, body {
    width: 1200px; height: 800px; overflow: hidden;
    background: var(--backdrop);
    font-family: "Open Sans", Arial, sans-serif;
  }
  .stage { position: relative; width: 1200px; height: 800px; }

  .card {
    position: absolute; top: 242px;
    width: 520px; height: 316px;
    box-shadow: 0 10px 30px rgba(0,0,0,.45);
    overflow: hidden;
  }

  /* Front */
  .card--front { left: 50px; background: var(--paper); }
  .front-frame {
    position: absolute; inset: 14px;
    border: 5px solid var(--ink);
  }
  .front-frame::after {
    content: ""; position: absolute; inset: 5px;
    border: 2px solid var(--ink);
  }
  .logo {
    position: absolute; left: 0; right: 0; top: 50%;
    transform: translateY(-50%);
    display: flex; align-items: center; justify-content: center; gap: 14px;
  }
  .logo-mark { width: 22px; height: 22px; background: var(--brand-blue); flex: none; }
  .logo-name {
    font-weight: 600; font-size: 44px; color: var(--ink);
    letter-spacing: .5px; line-height: 1; white-space: nowrap;
  }

  /* Back */
  .card--back { left: 630px; background: var(--charcoal); }
  .back-column {
    position: absolute; left: 0; top: 0; bottom: 0; width: 150px;
    background: var(--brand-blue);
  }
  .back-beacon {
    position: absolute; left: 58px; top: 172px; width: 72px; height: 144px;
    background: linear-gradient(180deg, var(--brand-blue-deep), #35547f);
    border-radius: 14px 14px 0 0;
  }
  .back-info {
    position: absolute; left: 46px; top: 24px; width: 448px; height: 118px;
    background: var(--paper-soft);
    display: flex; justify-content: space-between;
    padding: 14px 18px 0 18px;
  }
  .person-name { font-weight: 700; font-size: 15px; color: var(--brand-blue); white-space: nowrap; }
  .person-title { font-size: 11px; color: var(--ink-soft); margin-top: 1px; }
  .address { font-size: 11px; color: var(--ink-soft); margin-top: 20px; line-height: 1.35; white-space: nowrap; }
  .contacts { list-style: none; font-size: 11px; color: var(--ink-soft); line-height: 1.55; padding-top: 2px; white-space: nowrap; }
  .contacts b { color: var(--brand-blue); font-weight: 600; margin-right: 4px; }
  .back-band {
    position: absolute; left: 150px; right: 26px; top: 142px; height: 36px;
    background: var(--band);
  }
  .back-logo-panel {
    position: absolute; left: 150px; right: 26px; top: 178px; bottom: 22px;
    background: var(--paper-soft);
    display: flex; align-items: center; justify-content: center; gap: 10px;
  }
  .back-logo-panel .logo-mark { width: 16px; height: 16px; }
  .back-logo-panel .logo-name { font-size: 30px; }
</style>
</head>
<body>
<main class="stage">
  <section class="card card--front" aria-label="Card front">
    <div class="front-frame"></div>
    <div class="logo">
      <span class="logo-mark"></span>
      <span class="logo-name">Quillby Systems</span>
    </div>
  </section>

  <section class="card card--back" aria-label="Card back">
    <div class="back-column"></div>
    <div class="back-beacon" role="img" aria-label="Lighthouse illustration in deep blue"></div>
    <div class="back-info">
      <div class="identity">
        <p class="person-name">Dorian Vellacott</p>
        <p class="person-title">Owner</p>
        <p class="address">418 Bramlow Rd Unit C<br>Fernmoor, QS 02771</p>
      </div>
      <ul class="contacts">
        <li><b>T.</b>1.888.562.3907</li>
        <li><b>W.</b>www.quillbysys.example</li>
        <li><b>E.</b>dorian.v@quillbysys.example</li>
      </ul>
    </div>
    <div class="back-band"></div>
    <div class="back-logo-panel">
      <span class="logo-mark"></span>
      <span class="logo-name">Quillby Systems</span>
    </div>
  </section>
</main>
</body>
</html>
```